Wedding Marlies & Joost - Save the Date Wedding Card

I would like to have a creative save the date wedding card. We like grey/black/white colors and modern/ plain and simple.
I like the Save the Date copy big and book a flight copy smaller. I like stylish fonts for the save the date copy
Copy front:
Save the Date & book a flight
7-10-2017 Denia (Spanje)
Marlies & Joost
Onze dag is niet compleet zonder jou!
Copy back:
6-10 preferred travel date
7-10 wedding ceremony/drinks/dinner/party
8-10 hangover breakfast
Nearest Airports Valencia & Alicante
More info will be available soon!
wedding guests
Wedding

```html
<!DOCTYPE html>
<html lang="nl">
<head>
<meta charset="utf-8">
<title>Save the Date – Marlies &amp; Joost</title>
<link href="https://fonts.googleapis.com/css2?family=Great+Vibes&family=Pinyon+Script&family=Cormorant+Garamond:wght@500;600;700&display=swap" rel="stylesheet">
<style>
  :root {
    --page: #ececec;
    --card: #ffffff;
    --ink: #1e1e1e;
    --grey: #8a8a8a;
    --heart: #8c8c8c;
    --soft: #a6a6a6;
  }
  * { margin: 0; padding: 0; box-sizing: border-box; }
  html, body { width: 840px; height: 1200px; overflow: hidden; }
  body {
    background: var(--page);
    position: relative;
    font-family: "Cormorant Garamond", Georgia, serif;
    color: var(--ink);
  }
  .card {
    position: absolute;
    left: 80px;
    width: 680px;
    height: 453px;
    background: var(--card);
    box-shadow: 0 2px 10px rgba(0,0,0,0.12);
    text-align: center;
  }
  .card--front { top: 110px; }
  .card--back { top: 637px; }

  /* Front */
  .title {
    position: absolute;
    left: 0; right: 0; top: 60px;
    height: 130px;
  }
  .title__save, .title__date {
    position: absolute;
    top: 0;
    font-family: "Great Vibes", cursive;
    font-size: 100px;
    line-height: 1;
    color: var(--ink);
  }
  .title__save { left: 150px; }
  .title__date { left: 332px; }
  .title__the {
    position: absolute;
    left: 290px; top: -14px;
    font-family: "Great Vibes", cursive;
    font-size: 36px;
    line-height: 1;
    color: var(--grey);
  }
  .title__flight {
    position: absolute;
    left: 338px; top: 104px;
    font-size: 20px;
    font-weight: 600;
    font-variant: small-caps;
    letter-spacing: 1px;
    color: var(--soft);
  }
  .front__heart { position: absolute; left: 326px; top: 222px; }
  .front__date {
    position: absolute; left: 0; right: 0; top: 256px;
    font-size: 32px; font-weight: 700; letter-spacing: 1px; line-height: 1.2;
  }
  .front__place {
    position: absolute; left: 0; right: 0; top: 298px;
    font-size: 16px; font-weight: 700; font-variant: small-caps; letter-spacing: 1px;
  }
  .front__names {
    position: absolute; left: 0; right: 0; top: 340px;
    font-family: "Pinyon Script", cursive;
    font-size: 36px; line-height: 1.2;
  }
  .front__tagline {
    position: absolute; left: 0; right: 0; top: 404px;
    font-size: 20px; font-weight: 600; letter-spacing: 1px;
    color: var(--soft);
  }

  /* Back */
  .couple {
    position: absolute; left: 0; right: 0; top: 92px;
    display: flex; justify-content: center; align-items: center; gap: 12px;
  }
  .couple__dot {
    width: 14px; height: 14px; border-radius: 50%;
    background: var(--heart);
  }
  .couple__name {
    font-size: 32px; font-weight: 600; color: var(--ink); line-height: 1;
  }
  .schedule {
    position: absolute; left: 0; right: 0; top: 198px;
    list-style: none;
    font-size: 28px; font-weight: 600; font-variant: small-caps; line-height: 1.0;
  }
  .schedule li { height: 27px; }
  .travel {
    position: absolute; left: 0; right: 0; top: 342px;
    font-size: 18px; font-weight: 600; font-variant: small-caps; line-height: 1.2;
    color: var(--grey);
  }
</style>
</head>
<body>

<section class="card card--front">
  <div class="title">
    <span class="title__save">Save</span>
    <span class="title__the">the</span>
    <span class="title__date">Date</span>
    <span class="title__flight">&amp; book a flight</span>
  </div>
  <svg class="front__heart" width="28" height="25" viewBox="0 0 30 27" aria-hidden="true">
    <path d="M15 27 C6 19 0 14 0 7.5 C0 3 3.5 0 7.5 0 C11 0 13.5 2 15 5 C16.5 2 19 0 22.5 0 C26.5 0 30 3 30 7.5 C30 14 24 19 15 27 Z" fill="var(--heart)"/>
  </svg>
  <p class="front__date">7-10-2017</p>
  <p class="front__place">Denia (Spanje)</p>
  <p class="front__names">Marlies &amp; Joost</p>
  <p class="front__tagline">Onze dag is niet compleet zonder jou!</p>
</section>

<section class="card card--back">
  <div class="couple">
    <span class="couple__dot" aria-hidden="true"></span>
    <span class="couple__name">Marlies &amp; Joost</span>
  </div>
  <ul class="schedule">
    <li>6-10 optional late lunch</li>
    <li>7-10 wedding ceremony/drinks/dinner/party</li>
    <li>8-10 hangover breakfast</li>
  </ul>
  <p class="travel">Nearest Airports Valencia &amp; Alicante<br>More info will be available soon!</p>
</section>

</body>
</html>
```